TRB EVENTS & VISUALS WEBSITE DESIGN

Create a visually stimulating website for potential clients and vendors to effortlessly view our work. Sleek, classy vibe. Design should be clean, not too busy, yet visually enticing. Please refer to our old website and instagram for pictures and information. We still have our same philosophy & values, and our main goal is to create a fresh, new, inspiring look. (see below)

Website: www.trbeventsandvisuals.example
Instagram: trbeventsandvisuals

Target Market(s)

High end, Luxury wedding & event clients.

Industry/Entity Type

Event Planning

Number of Pages Required

5+ page

Font styles to use
Other font styles liked:
• Century Gothic

Colors

Designer to choose colors to be used in the design.

Requirements
Must have
• Lots of pictures/visual stimulation. Easy to access
• An abundance of photos capturing people, emotions, Beautiful event decor, & the venue itself.
Nice to have
• Trendy, up to date style
Should not have
• No detailed shots that show brand names

```html
<!DOCTYPE html>
<html lang="en">
<head>
<meta charset="utf-8">
<title>TRB Events &amp; Visuals</title>
<link href="https://fonts.googleapis.com/css2?family=Jost:wght@400;500;600&family=Open+Sans:wght@400;600&display=swap" rel="stylesheet">
<style>
:root{
  --navy:#1d3a78;
  --blue:#2e5aa8;
  --band:#1f4690;
  --footer:#2d5ba8;
  --footer-dark:#27509a;
  --orange:#e89d20;
  --white:#ffffff;
  --text:#555b66;
  --muted:#8a8f99;
}
*{margin:0;padding:0;box-sizing:border-box}
html,body{width:1200px;height:3066px;overflow:hidden;background:var(--white)}
body{position:relative;font-family:"Open Sans",sans-serif;color:var(--text)}
.abs{position:absolute}

/* hero */
.hero{left:0;top:0;width:1200px;height:684px;
  background:
    radial-gradient(ellipse 120px 90px at 600px 190px,rgba(255,225,255,.55),transparent 70%),
    radial-gradient(ellipse 70px 55px at 310px 250px,rgba(255,210,250,.35),transparent 70%),
    radial-gradient(ellipse 70px 55px at 890px 250px,rgba(255,210,250,.35),transparent 70%),
    radial-gradient(ellipse 160px 80px at 240px 420px,rgba(235,225,235,.35),transparent 70%),
    radial-gradient(ellipse 160px 80px at 980px 420px,rgba(235,225,235,.35),transparent 70%),
    radial-gradient(ellipse 260px 60px at 600px 440px,rgba(255,240,255,.28),transparent 70%),
    linear-gradient(180deg,rgba(20,6,30,.55) 0%,transparent 18%,transparent 62%,rgba(40,20,20,.7) 100%),
    radial-gradient(ellipse at 50% 40%,#b04ae0 0%,#7a2aa8 32%,#45166a 65%,#1e0b2c 100%)}
.nav a{position:absolute;top:52px;font-family:"Jost",sans-serif;font-weight:500;font-size:15px;color:var(--white);text-decoration:none;letter-spacing:.5px}
.nav .active{border:1.5px solid var(--white);border-right:none;border-bottom:none;padding:4px 0 0 6px;top:46px}
.brand{left:538px;top:22px;width:124px;text-align:center;color:var(--white);font-family:"Jost",sans-serif;font-weight:400}
.brand .big{font-size:50px;line-height:54px;letter-spacing:1px}
.brand .small{font-size:11px;letter-spacing:1px}
.hero-title{left:0;width:1200px;text-align:center;color:var(--white);font-family:"Jost",sans-serif;font-weight:600}
.hero-title.one{top:266px;font-size:68px;line-height:80px}
.hero-title.two{top:344px;font-size:48px;line-height:58px}
.rule{display:inline-block;width:46px;height:10px;border-top:3px solid #fff;border-bottom:3px solid #fff;vertical-align:middle;margin:0 6px}
.notch{left:520px;top:650px}
.hero-arrow{top:320px}

/* sections */
.section-title{left:0;width:1200px;text-align:center;font-family:"Jost",sans-serif;font-weight:600;font-size:35px;line-height:44px;color:var(--navy)}
.section-title span{display:inline-block;vertical-align:middle;width:38px;height:9px;border-top:3px solid currentColor;border-bottom:3px solid currentColor;margin:0 12px}

.service-card{top:799px;width:277px;height:268px}
.service-photo{width:100%;height:206px}
.service-label{position:relative;height:62px;background:var(--blue);color:var(--white);font-family:"Jost",sans-serif;font-weight:600;font-size:19px;line-height:19px;padding:12px 0 0 20px}
.service-label .go{position:absolute;right:0;top:0;width:56px;height:62px;background:var(--navy)}

.about-photo{left:276px;top:1157px;width:762px;height:418px;
  background:
    radial-gradient(ellipse 90px 160px at 700px 140px,rgba(255,220,150,.55),transparent 70%),
    radial-gradient(ellipse 130px 80px at 460px 40px,rgba(250,240,225,.6),transparent 70%),
    radial-gradient(ellipse 180px 200px at 430px 250px,rgba(230,190,160,.4),transparent 70%),
    linear-gradient(120deg,#2e1b0e,#7a4e26 40%,#c79a5e 68%,#4a2e16)}
.about-box{left:139px;top:1212px;width:428px;height:290px;background:var(--white);border-left:5px solid var(--blue);box-shadow:0 4px 18px rgba(0,0,0,.18);padding:28px 0 0 43px}
.about-box h2{font-family:"Jost",sans-serif;font-weight:600;font-size:32px;line-height:40px;color:var(--blue);margin-bottom:10px}
.about-box p{font-size:13.5px;line-height:24px;color:var(--text);white-space:nowrap}
.btn{display:inline-block;margin-top:12px;width:141px;height:37px;line-height:37px;text-align:center;background:var(--orange);color:var(--white);font-family:"Jost",sans-serif;font-weight:600;font-size:14px}

.venues{left:0;top:1670px;width:1200px;height:505px;
  background:
    radial-gradient(ellipse 220px 260px at 90px 260px,rgba(120,150,210,.25),transparent 70%),
    radial-gradient(ellipse 220px 260px at 1110px 260px,rgba(120,150,210,.25),transparent 70%),
    radial-gradient(ellipse 500px 120px at 600px 40px,rgba(140,170,230,.22),transparent 70%),
    var(--band)}
.venues-text{left:200px;top:1792px;width:800px;text-align:center;color:#dfe6f4;font-size:17px;line-height:24px}
.venue{box-shadow:0 6px 16px rgba(0,0,0,.35)}

.footer{left:0;top:2735px;width:1200px;height:263px;background:var(--footer)}
.footer-bar{left:0;top:2998px;width:1200px;height:68px;background:var(--footer-dark);color:#c9d6ee;text-align:center;font-size:13px;line-height:68px}
.footer-col h4{font-family:"Jost",sans-serif;font-weight:600;font-size:15px;color:var(--white);letter-spacing:.5px}
.footer-col h4::after{content:"";display:block;width:32px;height:2px;background:var(--white);margin-top:6px;margin-bottom:14px}
.footer-col li{list-style:none;color:var(--white);font-size:14px;line-height:26px}
.social{top:2836px;width:33px;height:33px;border:1.5px solid var(--white);border-radius:50%;display:flex;align-items:center;justify-content:center}
</style>
</head>
<body>

<header class="abs hero" role="img" aria-label="Ballroom lit in purple with chandeliers, floral centerpieces and set tables"></header>
<nav class="nav">
  <a class="active" style="left:172px">HOME</a>
  <a style="left:251px">ABOUT</a>
  <a style="left:327px">SERVICES</a>
  <a style="left:421px">VENUES</a>
  <a style="left:688px">AMAZING</a>
  <a style="left:787px">REVIEWS</a>
  <a style="left:875px">GALLERY</a>
  <a style="left:965px">CONTACT</a>
</nav>
<div class="abs brand"><div class="big">TRB</div><div class="small">EVENTS &amp; VISUALS</div></div>

<h1 class="abs hero-title one">WELCOME TO TRB</h1>
<div class="abs hero-title two"><span class="rule"></span>EVENT &amp; VISUALS<span class="rule"></span></div>

<svg class="abs hero-arrow" style="left:72px" width="24" height="40" viewBox="0 0 24 40"><path d="M20 4 L4 20 L20 36" fill="none" stroke="#fff" stroke-width="3"/></svg>
<svg class="abs hero-arrow" style="left:1104px" width="24" height="40" viewBox="0 0 24 40"><path d="M4 4 L20 20 L4 36" fill="none" stroke="#fff" stroke-width="3"/></svg>
<svg class="abs notch" width="160" height="36" viewBox="0 0 160 36"><path d="M0 36 C40 36 55 0 80 0 C105 0 120 36 160 36 Z" fill="#fff"/><path d="M70 12 L80 20 L90 12" fill="none" stroke="#8a8f99" stroke-width="2"/></svg>

<h2 class="abs section-title" style="top:720px"><span></span>OUR SERVICES<span></span></h2>
<svg class="abs" style="left:114px;top:916px" width="22" height="40" viewBox="0 0 22 40"><path d="M18 4 L4 20 L18 36" fill="none" stroke="#8a8f99" stroke-width="3"/></svg>
<svg class="abs" style="left:1062px;top:916px" width="22" height="40" viewBox="0 0 22 40"><path d="M4 4 L18 20 L4 36" fill="none" stroke="#8a8f99" stroke-width="3"/></svg>

<article class="abs service-card" style="left:162px">
  <div class="service-photo" role="img" aria-label="Tall floral centerpieces in a candlelit reception hall" style="background:radial-gradient(ellipse 90px 60px at 80px 80px,rgba(245,200,190,.7),transparent 70%),radial-gradient(ellipse 80px 60px at 210px 60px,rgba(240,180,170,.6),transparent 70%),radial-gradient(ellipse 140px 50px at 140px 175px,rgba(230,190,150,.45),transparent 70%),linear-gradient(160deg,#5a2430,#a86a5a 50%,#3d1c22)"></div>
  <div class="service-label">EVENT PLANNING<br>&amp; DESIGN<div class="go"><svg width="56" height="62" viewBox="0 0 56 62"><path d="M16 31 H40 M31 22 L40 31 L31 40" fill="none" stroke="#fff" stroke-width="2.5"/></svg></div></div>
</article>
<article class="abs service-card" style="left:462px">
  <div class="service-photo" role="img" aria-label="Couple dancing at a wedding reception surrounded by guests" style="background:radial-gradient(ellipse 60px 70px at 100px 150px,rgba(255,255,255,.85),transparent 70%),radial-gradient(ellipse 40px 60px at 180px 90px,rgba(230,230,230,.6),transparent 70%),linear-gradient(180deg,#3a3a3a,#6a6a6a 40%,#222 100%)"></div>
  <div class="service-label">PARTIAL EVENT<br>PLANNING<div class="go"><svg width="56" height="62" viewBox="0 0 56 62"><path d="M16 31 H40 M31 22 L40 31 L31 40" fill="none" stroke="#fff" stroke-width="2.5"/></svg></div></div>
</article>
<article class="abs service-card" style="left:761px">
  <div class="service-photo" role="img" aria-label="Live saxophonist and costumed performer on stage" style="background:radial-gradient(ellipse 50px 100px at 190px 130px,rgba(220,190,110,.8),transparent 70%),radial-gradient(ellipse 50px 40px at 185px 40px,rgba(245,240,225,.8),transparent 70%),radial-gradient(ellipse 60px 90px at 60px 130px,rgba(120,120,120,.6),transparent 70%),linear-gradient(180deg,#d8d8d8,#8a8a8a 45%,#2a2a2a)"></div>
  <div class="service-label">EVENT<br>PRODUCTION<div class="go"><svg width="56" height="62" viewBox="0 0 56 62"><path d="M16 31 H40 M31 22 L40 31 L31 40" fill="none" stroke="#fff" stroke-width="2.5"/></svg></div></div>
</article>

<div class="abs about-photo" role="img" aria-label="Bride and groom sharing a moment at a candlelit table"></div>
<section class="abs about-box">
  <h2>ABOUT US</h2>
  <p>Ascelerisque mi tortor at ipsum cligula augue<br>bibendum accumsan vestibulum ut<br>commodo a mi Morbi ornare gravida elit Integer<br>congue augue et malesuada iaculis ipsum dui aliquet<br>felis at cursus magna nisl nec elit Praesent</p>
  <a class="btn">READ MORE &rsaquo;</a>
</section>

<section class="abs venues" role="img" aria-label="Ornate ballroom interior in a blue tint"></section>
<h2 class="abs section-title" style="top:1738px;color:#fff"><span></span>OUR VENUES<span></span></h2>
<p class="abs venues-text">Ascelerisque mi tortor at ipsum cligula augue bibendum accumsan vestibulum ut<br>commodo a mi Morbi ornare gravida elit Integer congue augue e</p>
<div class="abs venue" role="img" aria-label="Empty venue hall with polished floor and tall windows" style="left:193px;top:1913px;width:254px;height:165px;background:radial-gradient(ellipse 60px 40px at 200px 60px,rgba(200,220,240,.7),transparent 70%),linear-gradient(180deg,#3a3f48,#5a6a80 35%,#2a2a2a 55%,#a07a4a)"></div>
<div class="abs venue" role="img" aria-label="Modern venue building at dusk on a street corner" style="left:756px;top:1913px;width:258px;height:165px;background:radial-gradient(ellipse 90px 30px at 130px 80px,rgba(240,210,140,.6),transparent 70%),linear-gradient(180deg,#5f8fd0,#3a5fa0 45%,#4a4a55)"></div>
<div class="abs venue" role="img" aria-label="Waterfront terrace at twilight overlooking a lit skyline" style="left:447px;top:1873px;width:309px;height:242px;background:radial-gradient(ellipse 120px 12px at 200px 118px,rgba(255,230,170,.6),transparent 70%),linear-gradient(180deg,#0e2a8a,#2e5ad0 45%,#7a5a6a 58%,#3a2e2e)"></div>

<h2 class="abs section-title" style="top:2216px"><span></span>OUR GALLERY<span></span></h2>
<div class="abs" role="img" aria-label="Bride and groom on a staircase" style="left:170px;top:2287px;width:190px;height:183px;background:radial-gradient(ellipse 50px 50px at 100px 140px,rgba(255,255,255,.9),transparent 70%),linear-gradient(160deg,#2f4a3a,#6a7a6a 55%,#cfd2cf)"></div>
<div class="abs" role="img" aria-label="Floral ceremony canopy with blue lighting" style="left:370px;top:2287px;width:190px;height:183px;background:radial-gradient(ellipse 90px 30px at 95px 25px,rgba(245,240,225,.8),transparent 70%),linear-gradient(180deg,#cfd8e8,#3a7ad0 55%,#1a3a8a)"></div>
<div class="abs" role="img" aria-label="Turquoise lit reception with tall centerpieces" style="left:566px;top:2287px;width:192px;height:183px;background:radial-gradient(ellipse 40px 40px at 96px 60px,rgba(240,250,255,.7),transparent 70%),linear-gradient(160deg,#0e6a8a,#2aa8c8 55%,#0a3a5a)"></div>
<div class="abs" role="img" aria-label="Bride and groom kissing in a ballroom" style="left:767px;top:2287px;width:271px;height:376px;background:radial-gradient(ellipse 90px 140px at 110px 290px,rgba(240,235,240,.85),transparent 70%),radial-gradient(ellipse 50px 40px at 220px 60px,rgba(230,180,200,.5),transparent 70%),linear-gradient(160deg,#2a2030,#5a3a5a 45%,#1e1a26)"></div>
<div class="abs" role="img" aria-label="Bridal portrait" style="left:170px;top:2480px;width:190px;height:183px;background:radial-gradient(ellipse 60px 50px at 95px 175px,rgba(255,255,255,.9),transparent 70%),linear-gradient(180deg,#d8d8d8,#4a4040 55%,#e0e0e0)"></div>
<div class="abs" role="img" aria-label="Bridesmaids in lavender dresses holding bouquets" style="left:370px;top:2480px;width:388px;height:183px;background:radial-gradient(ellipse 200px 60px at 194px 130px,rgba(170,150,190,.75),transparent 70%),linear-gradient(180deg,#c8ccc4,#7a8a6a 35%,#8a7a98 65%,#4a4a3e)"></div>

<footer class="abs footer"></footer>
<div class="abs" style="left:195px;top:2790px;width:130px;color:#fff;font-family:'Jost',sans-serif;font-weight:400;text-align:center">
  <div style="font-size:46px;line-height:50px">TRB</div><div style="font-size:11px;letter-spacing:1px">EVENTS &amp; VISUALS</div>
</div>
<div class="abs footer-col" style="left:427px;top:2789px"><h4>QUICK LINKS</h4><ul><li>HOME</li><li>ABOUT</li><li>SERVICES</li><li>VENUES</li></ul></div>
<div class="abs footer-col" style="left:610px;top:2789px"><h4>RESOURCES</h4><ul><li>AMAZING</li><li>REVIEWS</li><li>GALLERY</li><li>CONTACT</li></ul></div>
<div class="abs footer-col" style="left:782px;top:2789px"><h4>FOLLOW US</h4></div>
<div class="abs social" style="left:781px" aria-label="Email"><svg width="16" height="16" viewBox="0 0 16 16"><rect x="1.5" y="3.5" width="13" height="9" fill="none" stroke="#fff" stroke-width="1.4"/><path d="M1.5 3.5 L8 9 L14.5 3.5" fill="none" stroke="#fff" stroke-width="1.4"/></svg></div>
<div class="abs social" style="left:821px" aria-label="Website"><svg width="16" height="16" viewBox="0 0 16 16"><circle cx="8" cy="8" r="6.3" fill="none" stroke="#fff" stroke-width="1.4"/><path d="M1.7 8 H14.3 M8 1.7 C5 5 5 11 8 14.3 M8 1.7 C11 5 11 11 8 14.3" fill="none" stroke="#fff" stroke-width="1.2"/></svg></div>
<div class="abs social" style="left:862px" aria-label="Phone"><svg width="16" height="16" viewBox="0 0 16 16"><path d="M4 2 L6.5 2 L7.5 5 L6 6.3 C6.8 8 8 9.2 9.7 10 L11 8.5 L14 9.5 L14 12 C14 13 13 14 12 14 C6.5 13.5 2.5 9.5 2 4 C2 3 3 2 4 2 Z" fill="none" stroke="#fff" stroke-width="1.3"/></svg></div>
<div class="abs social" style="left:902px" aria-label="Location"><svg width="16" height="16" viewBox="0 0 16 16"><path d="M8 14.5 C5 10.5 3.5 8.3 3.5 6 A4.5 4.5 0 0 1 12.5 6 C12.5 8.3 11 10.5 8 14.5 Z" fill="none" stroke="#fff" stroke-width="1.4"/><circle cx="8" cy="6" r="1.6" fill="#fff"/></svg></div>
<div class="abs footer-bar">&copy; 2019 Company Name &nbsp;All right reserved</div>

</body>
</html>
```